Tallgrove Vale Management

I need a professional website. My current website is tallgrovevalemanagement.com and I hate it. It was created with some AI tool very quickly because I needed a site up and running with no advanced notice. I’m open to all designs .. I trust you, the professionals will deliver the results I’m anxiously awaiting! :)

```html
<!DOCTYPE html>
<html lang="en">
<head>
<meta charset="utf-8">
<title>Contact Us – Tallgrove Vale Management</title>
<link href="https://fonts.googleapis.com/css2?family=Heebo:wght@400;500;700&display=swap" rel="stylesheet">
<style>
:root{
  --navy:#0f2a4f;
  --navy-deep:#0b2243;
  --red:#cc1f24;
  --ink:#1b2940;
  --muted:#8a94a3;
  --line:#d9dee6;
  --light:#f3f5f8;
  --white:#ffffff;
}
*{box-sizing:border-box;margin:0;padding:0}
html,body{width:749px;height:1200px;overflow:hidden}
body{font-family:"Heebo",Arial,sans-serif;color:var(--ink);background:var(--white);position:relative}
.abs{position:absolute}
svg{display:block}

/* header */
.site-header{position:absolute;left:0;top:0;width:749px;height:67px;background:var(--white)}
.brand{position:absolute;left:24px;top:18px;width:100px;font-size:12px;font-weight:700;color:var(--navy);line-height:14px;text-transform:uppercase;letter-spacing:.5px}
.main-nav{position:absolute;left:151px;top:25px;display:flex;gap:0;font-size:9.5px;font-weight:500;color:var(--navy)}
.main-nav a{color:inherit;text-decoration:none;margin-right:25px;position:relative}
.main-nav a.active{color:var(--red)}
.main-nav a.active::after{content:"";position:absolute;left:0;right:0;top:19px;height:2px;background:var(--red)}
.phone-btn{position:absolute;left:614px;top:16px;width:108px;height:30px;background:var(--navy);border-radius:3px;color:var(--white);font-size:10px;font-weight:500;display:flex;align-items:center;justify-content:center;gap:6px}

/* hero */
.hero{position:absolute;left:0;top:67px;width:749px;height:278px;background:var(--navy-deep);overflow:hidden}
.hero-photo{position:absolute;left:300px;top:0;width:449px;height:278px;background:linear-gradient(180deg,#6f8fb6 0%,#9fb3c8 35%,#7a6a58 60%,#3f5a34 100%)}
.hero-photo::before{content:"";position:absolute;inset:0;background:linear-gradient(90deg,var(--navy-deep) 0%,rgba(11,34,67,.6) 22%,rgba(11,34,67,0) 50%)}
.eyebrow{position:absolute;left:43px;top:66px;font-size:10px;font-weight:500;color:var(--red);letter-spacing:.3px}
.eyebrow-rule{position:absolute;left:43px;top:87px;width:66px;height:2px;background:linear-gradient(90deg,var(--red) 60%,rgba(204,31,36,.3))}
.hero h1{position:absolute;left:43px;top:97px;font-size:27px;line-height:33px;font-weight:500;color:var(--white)}
.hero p{position:absolute;left:43px;top:174px;width:260px;font-size:10.5px;line-height:17px;color:#e4e9f1}

/* contact strip */
.contact-strip{position:absolute;left:0;top:345px;width:749px;height:152px;background:var(--light);display:flex}
.contact-item{flex:1;text-align:center;padding-top:23px;position:relative}
.contact-item + .contact-item::before{content:"";position:absolute;left:0;top:22px;bottom:20px;width:1px;background:var(--line)}
.contact-item:nth-child(1){flex:0 0 199px}
.contact-item:nth-child(2){flex:0 0 177px}
.contact-item:nth-child(3){flex:0 0 176px}
.icon-ring{width:34px;height:34px;border:1.5px solid var(--red);border-radius:50%;margin:0 auto;display:flex;align-items:center;justify-content:center;background:var(--white)}
.contact-item h3{margin-top:11px;font-size:11px;font-weight:500;color:var(--navy)}
.contact-item p{margin-top:4px;font-size:8.3px;line-height:14.5px;color:var(--ink)}

/* get in touch */
.touch-title{position:absolute;left:45px;top:518px;font-size:20px;font-weight:500;color:var(--navy)}
.touch-rule{position:absolute;left:45px;top:550px;width:30px;height:2px;background:var(--red)}
.touch-intro{position:absolute;left:45px;top:562px;width:200px;font-size:9.5px;line-height:16px;color:var(--ink)}
.reason{position:absolute;left:45px;width:242px;height:64px}
.reason-icon{position:absolute;left:0;top:0;width:39px;height:39px;border-radius:50%;background:var(--navy);display:flex;align-items:center;justify-content:center}
.reason h4{position:absolute;left:57px;top:1px;font-size:9px;font-weight:500;color:var(--navy)}
.reason p{position:absolute;left:57px;top:15px;width:180px;font-size:7.6px;line-height:13px;color:var(--ink)}
.reason-rule{position:absolute;left:45px;width:242px;height:1px;background:var(--line)}

/* form */
.contact-form{position:absolute;left:322px;top:522px;width:383px;height:346px;background:var(--white);border:1px solid #e6e9ee;border-radius:4px;box-shadow:0 2px 8px rgba(15,42,79,.06)}
.field-label{position:absolute;font-size:7.3px;color:var(--navy)}
.field-label .req{color:var(--red)}
.field{position:absolute;height:25px;border:1px solid var(--line);border-radius:2px;font-size:7.5px;color:var(--muted);padding:0 9px;display:flex;align-items:center}
.field.textarea{align-items:flex-start;padding-top:8px}
.send-btn{position:absolute;left:12px;top:302px;width:358px;height:31px;background:var(--red);border-radius:2px;color:var(--white);font-size:10px;font-weight:500;display:flex;align-items:center;justify-content:center;gap:8px}

/* cta band */
.cta-band{position:absolute;left:0;top:885px;width:749px;height:121px;background:var(--navy);border-bottom:1px solid #2a4468}
.cta-mark{position:absolute;left:70px;top:26px;width:54px;height:54px;border:2px solid var(--red);border-radius:50%}
.cta-band h2{position:absolute;left:153px;top:23px;font-size:18px;font-weight:500;color:var(--white)}
.cta-rule{position:absolute;left:153px;top:51px;width:31px;height:2px;background:var(--red)}
.cta-band p{position:absolute;left:153px;top:61px;width:280px;font-size:9.3px;line-height:14.5px;color:#e4e9f1}
.cta-btn{position:absolute;left:525px;top:48px;width:127px;height:34px;border:1px solid var(--white);border-radius:2px;color:var(--white);font-size:10px;font-weight:500;display:flex;align-items:center;justify-content:center;gap:7px}

/* footer */
.site-footer{position:absolute;left:0;top:1006px;width:749px;height:170px;background:var(--navy)}
.footer-brand{position:absolute;left:42px;top:30px;width:120px;font-size:12px;font-weight:700;line-height:14px;color:var(--white);text-transform:uppercase;letter-spacing:.5px}
.footer-tag{position:absolute;left:42px;top:85px;width:130px;font-size:8.7px;line-height:14.5px;color:#e4e9f1}
.social{position:absolute;top:140px;width:15px;height:15px;border-radius:50%;background:var(--white)}
.footer-col{position:absolute;top:20px}
.footer-col h5{font-size:10.5px;font-weight:500;color:var(--white);margin-bottom:10px}
.footer-col li{list-style:none;font-size:8.7px;line-height:16.6px;color:#e4e9f1}
.footer-divider{position:absolute;top:21px;width:1px;height:133px;background:#3a5478}
.info-row{display:flex;gap:8px;font-size:8.7px;line-height:14.5px;color:#e4e9f1;margin-bottom:6px}
.info-row svg{flex:0 0 auto;margin-top:3px}
.bottom-bar{position:absolute;left:0;top:1176px;width:749px;height:24px;background:var(--light);font-size:7.3px;color:var(--navy)}
.bottom-bar .copy{position:absolute;left:42px;top:7px}
.bottom-bar .legal{position:absolute;left:533px;top:7px;display:flex;gap:16px}
</style>
</head>
<body>

<header class="site-header">
  <div class="brand">Tallgrove<br>Vale<br>Management</div>
  <nav class="main-nav">
    <a href="#">Home</a><a href="#">About Us</a><a href="#">Our Services</a><a href="#">Owners</a><a href="#">Tenants</a><a href="#">Communities</a><a href="#" class="active">Contact Us</a>
  </nav>
  <div class="phone-btn">
    <svg width="10" height="10" viewBox="0 0 24 24"><path fill="#fff" d="M6.6 10.8a15.1 15.1 0 0 0 6.6 6.6l2.2-2.2c.3-.3.7-.4 1-.2 1.1.4 2.3.6 3.6.6.6 0 1 .4 1 1V20c0 .6-.4 1-1 1A17 17 0 0 1 3 4c0-.6.4-1 1-1h3.5c.6 0 1 .4 1 1 0 1.3.2 2.5.6 3.6.1.3 0 .7-.2 1z"/></svg>
    (555) 204-0188
  </div>
</header>

<section class="hero">
  <div class="hero-photo" role="img" aria-label="Photo of a tree-lined residential street with brick homes and a city skyline behind"></div>
  <div class="eyebrow">CONTACT US</div>
  <div class="eyebrow-rule"></div>
  <h1>Let’s Connect.<br>We’re Here to Help.</h1>
  <p>Whether you’re an owner looking for an experienced management partner or a tenant with a question, our team is ready to assist you.</p>
</section>

<section class="contact-strip">
  <div class="contact-item">
    <div class="icon-ring"><svg width="16" height="16" viewBox="0 0 24 24"><path fill="#cc1f24" d="M6.6 10.8a15.1 15.1 0 0 0 6.6 6.6l2.2-2.2c.3-.3.7-.4 1-.2 1.1.4 2.3.6 3.6.6.6 0 1 .4 1 1V20c0 .6-.4 1-1 1A17 17 0 0 1 3 4c0-.6.4-1 1-1h3.5c.6 0 1 .4 1 1 0 1.3.2 2.5.6 3.6.1.3 0 .7-.2 1z"/></svg></div>
    <h3>Call Us</h3>
    <p>(555) 204-0188<br>Mon – Fri: 9:00 AM – 5:00 PM</p>
  </div>
  <div class="contact-item">
    <div class="icon-ring"><svg width="16" height="12" viewBox="0 0 24 18"><rect x="1" y="1" width="22" height="16" rx="2" fill="#cc1f24"/><path d="M2 2l10 8 10-8" stroke="#fff" stroke-width="1.8" fill="none"/></svg></div>
    <h3>Email Us</h3>
    <p>info@tallgrovevalemanagement.com<br>We’ll respond within 1 business day.</p>
  </div>
  <div class="contact-item">
    <div class="icon-ring"><svg width="14" height="17" viewBox="0 0 20 26"><path fill="#cc1f24" d="M10 0a10 10 0 0 0-10 10c0 7.5 10 16 10 16s10-8.5 10-16A10 10 0 0 0 10 0z"/><circle cx="10" cy="10" r="3.6" fill="#fff"/></svg></div>
    <h3>Our Office</h3>
    <p>4200 Tallgrove Park Dr<br>Suite 200<br>Ridgeview, OH 44000</p>
  </div>
  <div class="contact-item">
    <div class="icon-ring"><svg width="16" height="16" viewBox="0 0 24 24"><circle cx="12" cy="12" r="10" fill="none" stroke="#cc1f24" stroke-width="2"/><path d="M12 6v6l4 3" stroke="#cc1f24" stroke-width="2" fill="none" stroke-linecap="round"/></svg></div>
    <h3>Office Hours</h3>
    <p>Monday – Friday<br>9:00 AM – 5:00 PM</p>
  </div>
</section>

<h2 class="touch-title">Get in Touch</h2>
<div class="touch-rule"></div>
<p class="touch-intro">Fill out the form and a member of our team will get back to you shortly.</p>

<div class="reason" style="top:607px">
  <div class="reason-icon"><svg width="20" height="20" viewBox="0 0 24 24" fill="none" stroke="#fff" stroke-width="1.5"><path d="M3 11l9-7 9 7"/><path d="M5 10v10h14V10"/><circle cx="12" cy="14" r="3"/><path d="M14 16l3 3"/></svg></div>
  <h4>For Property Owners</h4>
  <p>Learn how we can help you maximize returns and simplify property ownership.</p>
</div>
<div class="reason-rule" style="top:662px"></div>
<div class="reason" style="top:672px">
  <div class="reason-icon"><svg width="20" height="20" viewBox="0 0 24 24" fill="none" stroke="#fff" stroke-width="1.5"><circle cx="9" cy="8" r="3"/><circle cx="16" cy="9" r="2.5"/><path d="M3 19c0-3.3 2.7-6 6-6s6 2.7 6 6z"/><path d="M15 13.5c3 0 6 1.5 6 5h-5"/></svg></div>
  <h4>For Tenants</h4>
  <p>Questions about your application, lease, or maintenance? We’re here to help.</p>
</div>
<div class="reason-rule" style="top:727px"></div>
<div class="reason" style="top:736px">
  <div class="reason-icon"><svg width="20" height="20" viewBox="0 0 24 24" fill="none" stroke="#fff" stroke-width="1.5" stroke-linejoin="round"><path d="M2 9l4-3 4 2 3-2 4 1 5 3"/><path d="M2 9l3 5 5 4 3-1 5-4 4-4"/><path d="M9 12l3 3M11 11l3 3"/></svg></div>
  <h4>Partnerships</h4>
  <p>Interested in working with us? Let’s talk about opportunities to collaborate.</p>
</div>
<div class="reason-rule" style="top:791px"></div>
<div class="reason" style="top:800px">
  <div class="reason-icon"><svg width="20" height="20" viewBox="0 0 24 24" fill="none" stroke="#fff" stroke-width="1.6"><path d="M4 14v-2a8 8 0 0 1 16 0v2"/><rect x="3" y="13" width="4" height="6" rx="1.5"/><rect x="17" y="13" width="4" height="6" rx="1.5"/><path d="M19 19c0 2-2 3-6 3"/></svg></div>
  <h4>General Inquiries</h4>
  <p>Have a general question? Reach out and we’ll point you in the right direction.</p>
</div>

<form class="contact-form">
  <div class="field-label" style="left:12px;top:16px">First Name <span class="req">*</span></div>
  <div class="field" style="left:12px;top:31px;width:174px">First Name</div>
  <div class="field-label" style="left:195px;top:16px">Last Name <span class="req">*</span></div>
  <div class="field" style="left:195px;top:31px;width:175px">Last Name</div>

  <div class="field-label" style="left:12px;top:68px">Email Address <span class="req">*</span></div>
  <div class="field" style="left:12px;top:83px;width:174px">you@example.com</div>
  <div class="field-label" style="left:195px;top:68px">Phone Number</div>
  <div class="field" style="left:195px;top:83px;width:175px">(555) 123-4567</div>

  <div class="field-label" style="left:12px;top:121px">I am a <span class="req">*</span></div>
  <div class="field" style="left:12px;top:135px;width:358px;justify-content:space-between">Select an option
    <svg width="7" height="5" viewBox="0 0 10 6"><path d="M1 1l4 4 4-4" stroke="#1b2940" stroke-width="1.3" fill="none"/></svg></div>

  <div class="field-label" style="left:12px;top:174px">Subject <span class="req">*</span></div>
  <div class="field" style="left:12px;top:188px;width:358px">How can we help you?</div>

  <div class="field-label" style="left:12px;top:227px">Message <span class="req">*</span></div>
  <div class="field textarea" style="left:12px;top:241px;width:358px;height:51px">Please provide details so we can assist you better.</div>

  <div class="send-btn">Send Message
    <svg width="11" height="9" viewBox="0 0 14 10"><path d="M0 5h12M8 1l4 4-4 4" stroke="#fff" stroke-width="1.4" fill="none"/></svg></div>
</form>

<section class="cta-band">
  <div class="cta-mark"></div>
  <h2>We’re Here to Help You Succeed.</h2>
  <div class="cta-rule"></div>
  <p>At Tallgrove Vale Management, we believe in building strong relationships and delivering exceptional service. Contact us today and experience the difference.</p>
  <div class="cta-btn">
    <svg width="10" height="10" viewBox="0 0 24 24"><path fill="#fff" d="M6.6 10.8a15.1 15.1 0 0 0 6.6 6.6l2.2-2.2c.3-.3.7-.4 1-.2 1.1.4 2.3.6 3.6.6.6 0 1 .4 1 1V20c0 .6-.4 1-1 1A17 17 0 0 1 3 4c0-.6.4-1 1-1h3.5c.6 0 1 .4 1 1 0 1.3.2 2.5.6 3.6.1.3 0 .7-.2 1z"/></svg>
    Call Us Today
  </div>
</section>

<footer class="site-footer">
  <div class="footer-brand">Tallgrove<br>Vale<br>Management</div>
  <p class="footer-tag">We manage properties in the communities others won’t — and we do it better.</p>
  <span class="social" style="left:42px"></span>
  <span class="social" style="left:72px"></span>
  <span class="social" style="left:102px"></span>

  <div class="footer-col" style="left:220px">
    <h5>Quick Links</h5>
    <ul><li>Home</li><li>About Us</li><li>Our Services</li><li>Owners</li><li>Tenants</li><li>Communities</li><li>Contact Us</li></ul>
  </div>
  <div class="footer-divider" style="left:327px"></div>
  <div class="footer-col" style="left:359px">
    <h5>Our Services</h5>
    <ul><li>Property Management</li><li>Leasing &amp; Tenant Placement</li><li>HAP Contract Management</li><li>Inspection Coordination</li><li>Maintenance &amp; Repairs</li><li>Financial Reporting</li></ul>
  </div>
  <div class="footer-divider" style="left:505px"></div>
  <div class="footer-col" style="left:534px">
    <h5>Contact Info</h5>
    <div class="info-row"><svg width="9" height="9" viewBox="0 0 24 24"><path fill="#fff" d="M6.6 10.8a15.1 15.1 0 0 0 6.6 6.6l2.2-2.2c.3-.3.7-.4 1-.2 1.1.4 2.3.6 3.6.6.6 0 1 .4 1 1V20c0 .6-.4 1-1 1A17 17 0 0 1 3 4c0-.6.4-1 1-1h3.5c.6 0 1 .4 1 1 0 1.3.2 2.5.6 3.6.1.3 0 .7-.2 1z"/></svg>(555) 204-0188</div>
    <div class="info-row"><svg width="10" height="8" viewBox="0 0 24 18"><rect x="1" y="1" width="22" height="16" rx="1.5" fill="none" stroke="#fff" stroke-width="2"/><path d="M2 2l10 8 10-8" stroke="#fff" stroke-width="2" fill="none"/></svg>info@tallgrovevalemanagement.com</div>
    <div class="info-row"><svg width="9" height="11" viewBox="0 0 20 26"><path fill="none" stroke="#fff" stroke-width="2.2" d="M10 1a9 9 0 0 0-9 9c0 7 9 14.5 9 14.5s9-7.5 9-14.5a9 9 0 0 0-9-9z"/><circle cx="10" cy="10" r="3" fill="#fff"/></svg>4200 Tallgrove Park Dr<br>Suite 200<br>Ridgeview, OH 44000</div>
  </div>
</footer>

<div class="bottom-bar">
  <span class="copy">© 2025 Tallgrove Vale Management. All rights reserved.</span>
  <span class="legal"><span>Privacy Policy</span><span>|</span><span>Terms of Service</span></span>
</div>

</body>
</html>
```